New modern website for Kerbline Groundworks

Hi we are an existing company that has a current website http://www.kerblinegroundworks.co.nz/ we are looking to get a new vibrant looking website designed to take us further and gain more customers. We are after a simple easy to use website that does not confuse but we want to make an impact and stand out from the rest

Target Market(s)

Homeowners And Commercial Businesses

Industry/Entity Type

It Company

Coding

Coded - Design and coding required

Number of Pages Required

2 page

```html
<!DOCTYPE html>
<html lang="en">
<head>
<meta charset="utf-8">
<title>Kerbline Groundworks</title>
<link href="https://fonts.googleapis.com/css2?family=Raleway:wght@500;600;700&family=Open+Sans:wght@400;600&display=swap" rel="stylesheet">
<style>
:root{
  --lime:#c8c82a;
  --ink:#2b2b2b;
  --grey:#777;
  --dark:#1f1f1f;
  --line:#3a3a3a;
  --white:#fff;
}
*{box-sizing:border-box;margin:0;padding:0}
html,body{width:678px;height:1200px;overflow:hidden;background:#fff}
body{position:relative;font-family:"Open Sans",Arial,sans-serif;color:var(--ink)}
.abs{position:absolute}
.top-rule{left:0;top:0;width:678px;height:3px;background:var(--lime)}
.phone-tab{left:497px;top:0;width:128px;height:24px;background:var(--lime);border-radius:0 0 14px 14px;color:#fff;font:700 14px/24px Raleway,sans-serif;display:flex;align-items:center;justify-content:center;gap:5px}
.brand{font:700 14px Raleway,sans-serif;color:var(--ink);letter-spacing:.4px;display:flex;align-items:center;gap:6px;white-space:nowrap}
.header-brand{left:56px;top:24px}
.brand-dot{width:8px;height:8px;background:var(--ink);flex:none}
.nav{left:346px;top:34px;display:flex;gap:19px;font:600 8px Raleway,sans-serif;text-transform:uppercase;color:var(--ink)}
.nav .active{color:var(--lime)}
.hero{left:0;top:53px;width:678px;height:251px;background:linear-gradient(180deg,#4f6b3a 0%,#6e7f5b 40%,#59605a 60%,#7d8a5a 100%)}
.hero h1{position:absolute;top:76px;width:100%;text-align:center;font:700 23px/29px Raleway,sans-serif;color:#fff;text-shadow:0 1px 3px rgba(0,0,0,.5)}
.btn{position:absolute;left:278px;top:142px;width:123px;height:29px;background:var(--lime);color:#fff;font:700 8px/29px "Open Sans",sans-serif;text-align:center;border-radius:2px}
.dots{position:absolute;left:301px;top:219px;display:flex;gap:4px}
.dots i{width:16px;height:3px;background:#fff;border-radius:2px}
.dots i:first-child{background:var(--lime)}
.intro-title{top:328px;left:0;width:678px;text-align:center;font:700 13px Raleway,sans-serif}
.intro-text{left:105px;top:353px;width:468px;text-align:center;font:400 6.6px/13px "Open Sans",sans-serif;color:var(--grey)}
.feature{top:405px;width:132px;text-align:center}
.feature svg{display:block;margin:0 auto 10px}
.feature h3{font:600 8.6px Raleway,sans-serif;text-transform:uppercase;margin-bottom:8px;white-space:nowrap}
.feature p{font:400 6.4px/12px "Open Sans",sans-serif;color:var(--grey);padding:0 4px}
.services{left:0;top:528px;width:678px;height:202px;background:linear-gradient(180deg,#55524c 0%,#3a3a3a 50%,#2a2a2a 100%)}
.services h2{position:absolute;top:22px;width:100%;text-align:center;font:600 12px Raleway,sans-serif;color:#fff}
.service{position:absolute;top:58px;width:140px;text-align:center}
.service .ph{width:90px;height:90px;margin:0 auto 14px;background:rgba(255,255,255,.85);border-radius:4px}
.service h3{font:600 8.5px Raleway,sans-serif;color:#fff;text-transform:uppercase}
.projects-title{top:758px;left:0;width:678px;text-align:center;font:600 12.5px Raleway,sans-serif}
.thumb{top:786px;width:135px;height:97px;border:2px solid #e6e6e6}
.arrow{top:824px;width:21px;height:21px;border-radius:50%;background:#d6d6d6;color:#fff;font-size:10px;line-height:21px;text-align:center}
.cta{left:0;top:916px;width:678px;height:112px;background:var(--lime);color:#fff;text-align:center}
.cta h2{margin-top:34px;font:600 15px Raleway,sans-serif}
.cta .sub{margin-top:9px;font:600 9px "Open Sans",sans-serif}
.cta .nums{margin-top:4px;font:600 8.5px "Open Sans",sans-serif}
.cta .nums b{font:700 17px Raleway,sans-serif;vertical-align:-2px}
.footer{left:0;top:1028px;width:678px;height:172px;background:var(--dark);color:#ddd}
.footer-brand{left:44px;top:62px;color:#fff;font-size:11px}
.footer-brand .brand-dot{background:#fff;width:7px;height:7px}
.fcol{position:absolute;top:20px}
.fcol h4{font:600 8.5px Raleway,sans-serif;color:#fff;margin-bottom:15px}
.fcol li{list-style:none;font:400 6.5px "Open Sans",sans-serif;margin-bottom:9.5px}
.divider{position:absolute;top:20px;width:1px;height:122px;background:var(--line)}
.fcol p{font:400 6.5px/11px "Open Sans",sans-serif}
.email{width:148px;height:18px;background:#fff;color:#999;font:400 6.5px/18px "Open Sans",sans-serif;padding-left:8px;margin-top:7px}
.subscribe{display:inline-block;margin-top:8px;border:1px solid #fff;border-radius:3px;padding:5px 8px;font:700 6.5px "Open Sans",sans-serif;color:#fff}
.contact-row{display:flex;gap:9px;margin-bottom:12px;font:400 6.5px/11px "Open Sans",sans-serif}
.bottom-rule{position:absolute;left:46px;top:130px;width:586px;height:1px;background:var(--line)}
.copy{position:absolute;left:56px;top:147px;font:400 6.5px "Open Sans",sans-serif}
.social{position:absolute;left:537px;top:140px;display:flex;gap:5px}
.social i{width:18px;height:18px;border:1px solid #fff;border-radius:50%}
</style>
</head>
<body>
<header>
  <div class="abs top-rule"></div>
  <div class="abs phone-tab">
    <svg width="12" height="12" viewBox="0 0 24 24"><circle cx="12" cy="12" r="10" fill="none" stroke="#fff" stroke-width="2"/><path d="M9 7l2 3-1 1c1 2 2 3 4 4l1-1 3 2-1 2c-4 0-9-5-9-9z" fill="#fff"/></svg>
    09 555 0147
  </div>
  <div class="abs brand header-brand"><span class="brand-dot"></span>KERBLINE GROUNDWORKS</div>
  <nav class="abs nav">
    <span class="active">Home</span><span>About</span><span>Services</span><span>Projects</span><span>Contact Us</span>
    <svg width="8" height="8" viewBox="0 0 10 10"><circle cx="4" cy="4" r="3" fill="none" stroke="#2b2b2b" stroke-width="1.5"/><path d="M6 6l3 3" stroke="#2b2b2b" stroke-width="1.5"/></svg>
  </nav>
</header>

<section class="abs hero" role="img" aria-label="Paving crew laying fresh asphalt on a curved driveway beside green lawn">
  <h1>YOUR ONE-STOP SPECIALIST FOR<br>DRIVEWAY CONSTRUCTION IN AUCKLAND</h1>
  <div class="btn">GET MORE INFO &gt;&gt;</div>
  <div class="dots"><i></i><i></i><i></i><i></i></div>
</section>

<section class="intro">
  <h2 class="abs intro-title">THE TRUSTED NAME FOR ALL CONCRETE &amp; ASPHALT PAVING IN AUCKLAND</h2>
  <p class="abs intro-text">Leading the way for asphalt and concrete works throughout the Auckland region, Mark and the local team from Kerbline Groundworks will go the extra mile for your project. We can complete high quality asphalt paving, driveway construction and more for our clients. Ensuring the highest standards for safety and quality, we will work with you directly throughout all aspects of the job.</p>
  <div class="abs feature" style="left:47px">
    <svg width="30" height="30" viewBox="0 0 30 30"><rect x="2" y="13" width="6" height="14" fill="var(--lime)"/><path d="M10 13l5-10c2 0 3 1 3 3l-1 6h8c2 0 3 2 2 4l-3 10c-1 1-2 1-3 1H10z" fill="var(--lime)"/></svg>
    <h3>High Quality</h3><p>As part of our asphalt services, we are proud to offer a range of related services to our clients</p>
  </div>
  <div class="abs feature" style="left:197px">
    <svg width="30" height="30" viewBox="0 0 30 30"><circle cx="15" cy="9" r="7" fill="var(--lime)"/><path d="M3 29c0-8 5-12 12-12s12 4 12 12z" fill="var(--lime)"/></svg>
    <h3>Our Expertise</h3><p>We have a reputation with clients in and around Auckland for achieving great results on time</p>
  </div>
  <div class="abs feature" style="left:348px">
    <svg width="34" height="30" viewBox="0 0 34 30"><circle cx="12" cy="18" r="8" fill="none" stroke="var(--lime)" stroke-width="5" stroke-dasharray="3 2"/><circle cx="26" cy="8" r="5" fill="none" stroke="var(--lime)" stroke-width="4" stroke-dasharray="2.5 1.5"/></svg>
    <h3>Personalized Service</h3><p>Dedicated to quality results for your asphalt paving or driveway construction project</p>
  </div>
  <div class="abs feature" style="left:498px">
    <svg width="30" height="30" viewBox="0 0 30 30"><path d="M15 1l4 9 10 1-7.5 7 2 10-8.5-5-8.5 5 2-10L1 11l10-1z" fill="var(--lime)"/></svg>
    <h3>Years of Experience</h3><p>As part of our asphalt services, we are proud to offer a range of related services to our clients</p>
  </div>
</section>

<section class="abs services" role="img" aria-label="Winding dark asphalt road through open countryside">
  <h2>OUR SERVICES</h2>
  <div class="service" style="left:30px"><div class="ph" role="img" aria-label="Pickaxe over aggregate stones icon"></div><h3>Aggregates</h3></div>
  <div class="service" style="left:185px"><div class="ph" role="img" aria-label="Traffic cone icon"></div><h3>Paving &amp; Construction</h3></div>
  <div class="service" style="left:341px"><div class="ph" role="img" aria-label="Concrete mixer truck icon"></div><h3>Ready-Mixed Concrete</h3></div>
  <div class="service" style="left:496px"><div class="ph" role="img" aria-label="Tracked bulldozer icon"></div><h3>Asphalt</h3></div>
</section>

<section class="projects">
  <h2 class="abs projects-title">OUR PROJECTS</h2>
  <div class="abs arrow" style="left:36px">&#8249;</div>
  <div class="abs thumb" style="left:55px;background:linear-gradient(180deg,#8a7a6a,#b9bcc0)" role="img" aria-label="Crew finishing a wet concrete slab"></div>
  <div class="abs thumb" style="left:199px;background:linear-gradient(180deg,#9a8c6a,#8b8170)" role="img" aria-label="Concrete truck pouring on a work site"></div>
  <div class="abs thumb" style="left:343px;background:linear-gradient(180deg,#6f7a5a,#707468)" role="img" aria-label="Freshly sealed asphalt surface"></div>
  <div class="abs thumb" style="left:487px;background:linear-gradient(180deg,#4e6238,#8d9080)" role="img" aria-label="New driveway lined with garden plants"></div>
  <div class="abs arrow" style="left:621px">&#8250;</div>
</section>

<section class="abs cta">
  <h2>ANY QUESTIONS YOU WOULD LIKE TO ASK?</h2>
  <div class="sub">Need to talk to us... Contact us on</div>
  <div class="nums">MOBILE: <b>027 555 0192</b> OR PHONE: <b>09 555 0147</b></div>
</section>

<footer class="abs footer">
  <div class="abs brand footer-brand"><span class="brand-dot"></span>KERBLINE GROUNDWORKS</div>
  <div class="divider" style="left:216px"></div>
  <div class="fcol" style="left:234px">
    <h4>INFORMATION</h4>
    <ul><li>Home</li><li>About</li><li>Services</li><li>Projects</li><li>Contact Us</li></ul>
  </div>
  <div class="divider" style="left:314px"></div>
  <div class="fcol" style="left:332px">
    <h4>NEWSLETTER</h4>
    <p>Register your email address to get<br>information about us</p>
    <div class="email">Email Address</div>
    <span class="subscribe">SUBSCRIBE</span>
  </div>
  <div class="divider" style="left:496px"></div>
  <div class="fcol" style="left:514px">
    <h4>CONTACT US</h4>
    <div class="contact-row"><svg width="6" height="9" viewBox="0 0 6 9"><path d="M3 0a3 3 0 0 1 3 3c0 2-3 6-3 6S0 5 0 3a3 3 0 0 1 3-3z" fill="#fff"/></svg><span>27 Quarry Lane, Unit 5,<br>Auckland 1061</span></div>
    <div class="contact-row"><svg width="7" height="9" viewBox="0 0 24 24"><path d="M6 2l4 5-2 2c1 3 3 5 6 6l2-2 5 4-2 4C10 21 3 14 3 4z" fill="#fff"/></svg><span>09 555 0147</span></div>
    <div class="contact-row"><svg width="9" height="8" viewBox="0 0 9 7"><rect width="9" height="7" fill="#fff"/><path d="M0 0l4.5 4L9 0" fill="none" stroke="#1f1f1f" stroke-width=".8"/></svg><span>info@kerblinegroundworks.co.nz</span></div>
  </div>
  <div class="bottom-rule"></div>
  <div class="copy">Copyrights © 2016, Kerbline Groundworks. All rights reserved.</div>
  <div class="social" aria-label="Social links"><i></i><i></i><i></i><i></i></div>
</footer>
</body>
</html>
```